Website for legal expungement services with button to qualify/disqualify potential clients

Larkfield Record Relief, LLC is a law firm focusing in legal expungement servcies (allowing people to erase criminal court records, police records, proseution files, etc). I want a more modern look which exudes confidence in the services. I am looking for a clean website that looks very polished. I want to keep the pages to a minimum, as I want the page not so much to answer questions, but to direct traffic to contact the law office. I would like the main focus point to be an button which would take a client through a series of questions to see if they would qualify for the services; this serves two purposes 1) to collect contact info for future marketing via email and 2) eliminate individuals who we are currently unable to help. A current theme that I have played around with are "Change so much, you'll need to reintroduce yourself" alongside a picture of a guys hand outstretched.
On the landing page, I would like a very brief and to the point explanation of what the service would be (i.e. "Leave your past in the past; expunge all your criminal records" ), followed by a list of benefits that it provides. (NB: included is a file "law post card-02" that includes the main benefits to expungement). Also included are two logo files for a more updated logo I currently use ("LRR Logo" and LRR Logo2") (NB: I'm open to revisions on this as well). Lastly, I've had two very minor 'ads' that I did ("postcard back" and "HVC Ad") that I like the idea of.

Target Market(s)

Middle/upper-middle class, mostly male, people with a criminal record or criminal accusation

Industry/Entity Type

Legal Services

Coding

Coded - Design and coding required

Requirements
Must have
• Button that attracts attention up front (possibly stand out coloring) to click to open up a series of questions to qualify/eliminate prospects, and simultaneously gather their info. Also, must be mobile friendly.

```html
<!DOCTYPE html>
<html lang="en">
<head>
<meta charset="utf-8">
<title>Larkfield Record Relief, LLC</title>
<link href="https://fonts.googleapis.com/css2?family=Libre+Baskerville:wght@400;700&family=Inter:wght@400;500;600;700&display=swap" rel="stylesheet">
<style>
:root{
  --navy:#0a3a78;
  --navy-deep:#0e2340;
  --gold:#d4a62a;
  --sky:#cfe6f9;
  --mist:#eef2f7;
  --ink:#111;
  --text:#3a3f4a;
  --line:#c9d3e1;
  --white:#fff;
}
*{box-sizing:border-box;margin:0;padding:0}
html,body{width:1200px;height:4110px;overflow:hidden}
body{position:relative;background:var(--white);font-family:"Inter",Arial,sans-serif;color:var(--text)}
.abs{position:absolute}
.serif{font-family:"Libre Baskerville",Georgia,serif;color:var(--ink);font-weight:700}
.btn{position:absolute;display:flex;align-items:center;justify-content:center;width:226px;height:54px;background:var(--navy);color:#fff;font-size:15px;font-weight:700;letter-spacing:1px}
.btn.gold{background:var(--gold)}
.brand{font-family:"Libre Baskerville",Georgia,serif;font-size:17px;font-weight:700;color:var(--navy);letter-spacing:.5px}
.photo{position:absolute}
.dots{position:absolute;background-image:radial-gradient(var(--line) 1.6px,transparent 1.8px);background-size:9px 9px}

.site-header{position:absolute;left:0;top:0;width:1200px;height:105px}
.site-header .brand{left:85px;top:40px}
.nav a{position:absolute;top:43px;font-size:14px;color:#555;text-decoration:none}
.nav a.active{color:var(--navy);font-weight:600}
.phone-box{position:absolute;width:46px;height:46px;background:var(--gold);display:flex;align-items:center;justify-content:center}
.contact-label{position:absolute;font-size:13px;color:#666}
.contact-number{position:absolute;font-size:18px;font-weight:700;color:var(--navy)}

.hero{position:absolute;left:0;top:105px;width:1200px;height:596px;background:var(--sky);overflow:hidden}
.kicker{position:absolute;left:85px;top:158px;font-size:19px;font-weight:600;letter-spacing:3px;color:var(--ink)}
.hero h1{position:absolute;left:85px;top:200px;font-size:62px;line-height:68px}

.checklist{position:absolute;list-style:none}
.checklist li{position:relative;height:41px;font-size:16px;color:#333;padding-left:58px;line-height:20px}
.checklist li svg{position:absolute;left:0;top:2px}
.checklist::before{content:"";position:absolute;left:37px;top:0;bottom:14px;border-left:1px solid var(--line)}

.flow-section{position:absolute;left:0;top:2131px;width:1200px;height:830px;background:var(--mist)}
.flow-label{position:absolute;width:230px;text-align:center;font-size:16px;line-height:32px;color:#444}
.node{position:absolute;width:146px;height:146px;border-radius:50%;border:1.5px solid var(--line);display:flex;align-items:center;justify-content:center}
.node .core{width:106px;height:106px;border-radius:50%;background:#fff;box-shadow:0 6px 16px rgba(10,58,120,.10);display:flex;align-items:center;justify-content:center}
.tag{position:absolute;width:66px;height:20px;border-radius:10px;background:#c8d4e6;color:var(--navy);font-size:12px;text-align:center;line-height:20px;font-weight:700}

.site-footer{position:absolute;left:0;top:3540px;width:1200px;height:570px;background:var(--navy-deep)}
.site-footer .serif{color:#fff}
.foot-link{position:absolute;font-size:15px;color:#4e6383}
.social{position:absolute;width:48px;height:48px;background:#1d3457}
</style>
</head>
<body>

<header class="site-header">
  <div class="abs brand">Larkfield Record Relief</div>
  <nav class="nav">
    <a class="active" style="left:432px">Benefits of Expungement</a>
    <a style="left:646px">What Type of Cases</a>
    <a style="left:822px">Records</a>
  </nav>
  <div class="phone-box" style="left:930px;top:28px">
    <svg width="22" height="22" viewBox="0 0 24 24" fill="none" stroke="#fff" stroke-width="1.8"><path d="M5 3h4l2 5-2.5 1.5a11 11 0 0 0 6 6L16 13l5 2v4a2 2 0 0 1-2 2A16 16 0 0 1 3 5a2 2 0 0 1 2-2z"/></svg>
  </div>
  <div class="contact-label" style="left:992px;top:30px">Contact us:</div>
  <div class="contact-number" style="left:992px;top:55px">555-014-2290</div>
</header>

<section class="hero">
  <svg class="abs" style="left:0;top:0" width="1200" height="596" viewBox="0 0 1200 596">
    <path d="M377 0H1200V596H620C520 520 470 380 455 250C440 140 410 60 377 0Z" fill="var(--navy)"/>
    <rect x="583" y="150" width="200" height="440" rx="100" fill="#0b3f82"/>
    <rect x="990" y="65" width="86" height="420" rx="43" fill="var(--gold)"/>
    <rect x="700" y="170" width="120" height="300" rx="60" fill="var(--gold)"/>
  </svg>
  <div class="photo" role="img" aria-label="Smiling man in suit and glasses offering a handshake" style="left:670px;top:10px;width:400px;height:586px;background:linear-gradient(180deg,#3a4e68 0%,#1f2d40 55%,#25406e 100%);border-radius:140px 140px 0 0"></div>
  <div class="kicker">CHANGE SO MUCH,</div>
  <h1 class="serif">You'll need to<br>reintroduce<br>yourself</h1>
  <div class="btn" style="left:85px;top:455px">VIEW YOUR QUERIES</div>
</section>
<div class="abs" style="left:203px;top:655px;width:2px;height:55px;background:var(--navy)"></div>
<div class="abs" style="left:203px;top:710px;width:2px;height:52px;background:var(--gold)"></div>

<section>
  <div class="abs" style="left:190px;top:850px;width:313px;height:410px;border:2px solid var(--line)"></div>
  <div class="abs" style="left:85px;top:1080px;width:115px;height:225px;background:var(--gold);clip-path:polygon(0 0,100% 100%,0 100%)"></div>
  <div class="abs" style="left:85px;top:1080px;width:12px;height:225px;background:var(--gold)"></div>
  <div class="abs" style="left:85px;top:1293px;width:113px;height:12px;background:var(--gold)"></div>
  <div class="photo" role="img" aria-label="Wooden judge's gavel resting on its block" style="left:97px;top:904px;width:351px;height:389px;background:linear-gradient(135deg,#d8d8d8,#8a8a8a 45%,#6b3b22 70%,#c9c9c9)"></div>
  <div class="dots" style="left:336px;top:885px;width:130px;height:55px"></div>
  <h2 class="serif abs" style="left:622px;top:866px;font-size:52px;line-height:64px">How your<br>records are seen<br>by the public</h2>
  <ul class="checklist" style="left:622px;top:1097px">
    <li><svg width="18" height="18" viewBox="0 0 18 18"><circle cx="9" cy="9" r="8" fill="var(--navy)"/><path d="M5 9l3 3 5-6" stroke="#fff" stroke-width="2" fill="none"/></svg>Public reporting (www.statecourts-portal.org)</li>
    <li><svg width="18" height="18" viewBox="0 0 18 18"><circle cx="9" cy="9" r="8" fill="var(--navy)"/><path d="M5 9l3 3 5-6" stroke="#fff" stroke-width="2" fill="none"/></svg>Police reports</li>
    <li><svg width="18" height="18" viewBox="0 0 18 18"><circle cx="9" cy="9" r="8" fill="var(--navy)"/><path d="M5 9l3 3 5-6" stroke="#fff" stroke-width="2" fill="none"/></svg>State department of public safety</li>
    <li><svg width="18" height="18" viewBox="0 0 18 18"><circle cx="9" cy="9" r="8" fill="var(--navy)"/><path d="M5 9l3 3 5-6" stroke="#fff" stroke-width="2" fill="none"/></svg>District attorney prosecution files</li>
    <li><svg width="18" height="18" viewBox="0 0 18 18"><circle cx="9" cy="9" r="8" fill="var(--navy)"/><path d="M5 9l3 3 5-6" stroke="#fff" stroke-width="2" fill="none"/></svg>Court records</li>
  </ul>
</section>

<section>
  <h2 class="serif abs" style="left:0;width:1200px;text-align:center;top:1408px;font-size:52px">The benefits of expungement</h2>
  <div class="abs" style="left:85px;top:1535px;width:815px;height:483px;border:2px solid var(--line)"></div>
  <div class="abs" style="left:132px;top:1580px;width:80px;height:80px;border-radius:50%;background:var(--gold);display:flex;align-items:center;justify-content:center">
    <svg width="40" height="40" viewBox="0 0 40 40" fill="none" stroke="#fff" stroke-width="2.5"><circle cx="15" cy="15" r="8"/><circle cx="25" cy="25" r="8"/></svg>
  </div>
  <p class="abs" style="left:132px;top:1684px;width:410px;font-size:15.5px;line-height:32.6px;color:#333">Larkfield Record Relief is 5-star rated firm, which has been formed&nbsp; with the passing of the State Expungement law of 2020. It is a subdivision of the Halden law firm, and since its creation has helped over 100 local citizens successfully expunge their criminal records.</p>
  <div class="btn" style="left:132px;top:1920px">VIEW YOUR QUERIES</div>
  <div class="dots" style="left:633px;top:1575px;width:130px;height:55px"></div>
  <div class="abs" style="left:1114px;top:1645px;width:26px;height:100px;background:var(--gold)"></div>
  <div class="abs" style="left:1114px;top:1697px;width:86px;height:265px;background:var(--navy)"></div>
  <div class="photo" role="img" aria-label="Lawyer in suit signing documents at a desk with scales and gavel" style="left:650px;top:1591px;width:464px;height:371px;background:linear-gradient(135deg,#3b4f68,#6c7f96 40%,#8a5a34 80%,#5a3b23);box-shadow:0 10px 24px rgba(0,0,0,.15)"></div>
  <div class="abs" style="left:897px;top:1972px;width:2px;height:46px;background:#fff"></div>
</section>

<section class="flow-section">
  <h2 class="serif abs" style="left:0;width:1200px;text-align:center;top:100px;font-size:52px">Benefits to expunging</h2>
  <div class="flow-label" style="left:100px;top:220px">Better job opportunities<br>leading to higher income</div>
  <div class="flow-label" style="left:356px;top:220px">Loan qualification and<br>better loan rates</div>
  <div class="flow-label" style="left:613px;top:220px">Protecting yours<br>privacy</div>
  <div class="flow-label" style="left:869px;top:220px">Better education<br>opportunities</div>

  <svg class="abs" style="left:0;top:0" width="1200" height="830">
    <g stroke="#9fb0c8" stroke-width="1.5" fill="none">
      <path d="M1057 402h25a30 30 0 0 1 30 30v75a30 30 0 0 1-30 30h-25"/>
      <path d="M288 402h80M544 402h80M801 402h80"/>
      <path d="M288 537h80M544 537h80M801 537h80"/>
    </g>
    <g stroke="var(--navy)" stroke-width="1.8" fill="none">
      <path d="M298 402h20m-6-6 6 6-6 6"/><path d="M590 402h20m-6-6 6 6-6 6"/><path d="M847 402h20m-6-6 6 6-6 6"/>
      <path d="M352 537h-20m6-6-6 6 6 6"/><path d="M608 537h-20m6-6-6 6 6 6"/><path d="M865 537h-20m6-6-6 6 6 6"/>
    </g>
  </svg>

  <div class="node" style="left:142px;top:329px"><div class="core"><svg width="44" height="44" viewBox="0 0 44 44"><circle cx="18" cy="12" r="7" fill="var(--navy)"/><path d="M5 38c0-9 6-14 13-14s10 3 12 7v7z" fill="var(--navy)"/><rect x="25" y="27" width="14" height="11" rx="2" fill="var(--gold)"/></svg></div></div>
  <div class="node" style="left:398px;top:329px"><div class="core"><svg width="44" height="44" viewBox="0 0 44 44"><path d="M14 10h10l-3 6c8 3 10 12 8 20H9c-2-8 0-17 8-20z" fill="var(--navy)"/><circle cx="30" cy="31" r="7" fill="var(--gold)"/></svg></div></div>
  <div class="node" style="left:655px;top:329px"><div class="core"><svg width="44" height="44" viewBox="0 0 44 44"><rect x="8" y="6" width="20" height="28" rx="2" fill="var(--navy)"/><path d="M12 13h12M12 19h12M12 25h8" stroke="#fff" stroke-width="2"/><path d="M30 20l8 3v6c0 5-4 8-8 10-4-2-8-5-8-10v-6z" fill="var(--gold)"/></svg></div></div>
  <div class="node" style="left:911px;top:329px"><div class="core"><svg width="44" height="44" viewBox="0 0 44 44"><path d="M22 9l18 8-18 8-18-8z" fill="var(--navy)"/><path d="M11 21v8c0 3 5 5 11 5s11-2 11-5v-8l-11 5z" fill="var(--gold)"/></svg></div></div>

  <div class="node" style="left:142px;top:464px"><div class="core"><svg width="44" height="44" viewBox="0 0 44 44"><circle cx="15" cy="9" r="5" fill="var(--navy)"/><path d="M10 16l10 2 4 8-4 2-3-5-2 7 5 8-3 2-6-8-4 8-3-2 4-10z" fill="var(--navy)"/><path d="M29 12l8 3v6c0 5-4 7-8 9-4-2-8-4-8-9v-6z" fill="var(--gold)"/></svg></div></div>
  <div class="node" style="left:398px;top:464px"><div class="core"><svg width="44" height="44" viewBox="0 0 44 44"><path d="M22 8L5 23h5v14h24V23h5z" fill="var(--navy)"/><path d="M22 8L5 23h4L22 12l13 11h4z" fill="var(--gold)"/><rect x="18" y="27" width="8" height="10" fill="#fff"/></svg></div></div>
  <div class="node" style="left:655px;top:464px"><div class="core"><svg width="44" height="44" viewBox="0 0 44 44"><circle cx="22" cy="11" r="5" fill="var(--navy)"/><circle cx="12" cy="18" r="4" fill="var(--navy)"/><circle cx="32" cy="18" r="4" fill="var(--navy)"/><path d="M14 36c0-8 4-12 8-12s8 4 8 12z" fill="var(--gold)"/><path d="M5 34c0-6 3-10 7-10l2 10zM39 34c0-6-3-10-7-10l-2 10z" fill="var(--navy)"/></svg></div></div>
  <div class="node" style="left:911px;top:464px"><div class="core"><svg width="44" height="44" viewBox="0 0 44 44"><circle cx="18" cy="12" r="7" fill="var(--navy)"/><path d="M5 38c0-9 6-14 13-14 3 0 5 1 7 2v12z" fill="var(--navy)"/><path d="M31 22l8 3v6c0 5-4 7-8 9-4-2-8-4-8-9v-6z" fill="var(--gold)"/></svg></div></div>

  <div class="tag" style="left:182px;top:325px">›</div>
  <div class="tag" style="left:438px;top:325px">›</div>
  <div class="tag" style="left:695px;top:325px">›</div>
  <div class="tag" style="left:951px;top:325px">›</div>
  <div class="tag" style="left:182px;top:599px">›</div>
  <div class="tag" style="left:438px;top:599px">›</div>
  <div class="tag" style="left:695px;top:599px">›</div>
  <div class="tag" style="left:951px;top:599px">›</div>

  <div class="flow-label" style="left:100px;top:658px">Removing the stigma of<br>having a criminal record</div>
  <div class="flow-label" style="left:356px;top:658px">More option for<br>housing</div>
  <div class="flow-label" style="left:598px;top:658px;width:260px">Qualifying for government<br>assistance programs</div>
  <div class="flow-label" style="left:869px;top:658px">Lower insurance<br>premiums</div>
</section>

<section>
  <h2 class="serif abs" style="left:85px;top:3060px;font-size:52px;line-height:64px">What types<br>of cases qualify:</h2>
  <ul class="checklist" style="left:85px;top:3231px">
    <li><svg width="18" height="18" viewBox="0 0 18 18"><circle cx="9" cy="9" r="8" fill="var(--navy)"/><path d="M5 9l3 3 5-6" stroke="#fff" stroke-width="2" fill="none"/></svg>Criminal acusations that were dismissed</li>
    <li><svg width="18" height="18" viewBox="0 0 18 18"><circle cx="9" cy="9" r="8" fill="var(--navy)"/><path d="M5 9l3 3 5-6" stroke="#fff" stroke-width="2" fill="none"/></svg>Criminal cases that went into a diversionary program</li>
    <li><svg width="18" height="18" viewBox="0 0 18 18"><circle cx="9" cy="9" r="8" fill="var(--navy)"/><path d="M5 9l3 3 5-6" stroke="#fff" stroke-width="2" fill="none"/></svg>Convictions</li>
  </ul>
  <div class="btn gold" style="left:85px;top:3375px">VIEW YOUR QUERIES</div>
  <div class="phone-box" style="left:328px;top:3379px;background:#e3eaf4">
    <svg width="22" height="22" viewBox="0 0 24 24" fill="none" stroke="var(--navy)" stroke-width="1.8"><path d="M5 3h4l2 5-2.5 1.5a11 11 0 0 0 6 6L16 13l5 2v4a2 2 0 0 1-2 2A16 16 0 0 1 3 5a2 2 0 0 1 2-2z"/></svg>
  </div>
  <div class="contact-label" style="left:390px;top:3376px">Contact us:</div>
  <div class="contact-number" style="left:390px;top:3400px">555-014-2290</div>
  <div class="dots" style="left:620px;top:3335px;width:130px;height:120px"></div>
  <div class="photo" role="img" aria-label="Reading glasses and a wooden gavel on a desk" style="left:645px;top:3072px;width:470px;height:356px;background:linear-gradient(135deg,#c9a87a,#e7d8c0 45%,#f2efe9 60%,#5a3421)"></div>
</section>

<footer class="site-footer">
  <div class="serif abs" style="left:85px;top:107px;font-size:24px;line-height:33px">Join our<br>community subscribe us:</div>
  <div class="abs" style="left:598px;top:132px;font-size:15px;color:#6e819d">Email address:</div>
  <div class="abs" style="left:598px;top:170px;width:516px;height:1px;background:#3b5275"></div>
  <div class="phone-box" style="left:1068px;top:112px">
    <svg width="22" height="22" viewBox="0 0 24 24" fill="none" stroke="#fff" stroke-width="2"><path d="M4 12h15m-6-6 6 6-6 6"/></svg>
  </div>

  <div class="abs brand" style="left:85px;top:300px;color:#fff">Larkfield Record Relief</div>
  <div class="social" style="left:85px;top:340px" aria-label="Social profile"></div>
  <div class="social" style="left:145px;top:340px" aria-label="Social profile"></div>
  <div class="social" style="left:205px;top:340px" aria-label="Social profile"></div>

  <div class="serif abs" style="left:554px;top:265px;font-size:18px">Quick Links</div>
  <div class="foot-link" style="left:554px;top:320px">Benefits of Expungement</div>
  <div class="foot-link" style="left:554px;top:353px">What Type of Cases</div>
  <div class="foot-link" style="left:554px;top:386px">Records</div>

  <div class="serif abs" style="left:930px;top:265px;font-size:18px">Contact us</div>
  <svg class="abs" style="left:930px;top:320px" width="18" height="18" viewBox="0 0 24 24" fill="none" stroke="var(--gold)" stroke-width="2"><path d="M5 3h4l2 5-2.5 1.5a11 11 0 0 0 6 6L16 13l5 2v4a2 2 0 0 1-2 2A16 16 0 0 1 3 5a2 2 0 0 1 2-2z"/></svg>
  <div class="foot-link" style="left:968px;top:320px">555-014-2290</div>
  <svg class="abs" style="left:930px;top:370px" width="18" height="18" viewBox="0 0 24 24" fill="none" stroke="var(--gold)" stroke-width="2"><rect x="3" y="5" width="18" height="14"/><path d="M3 6l9 7 9-7"/></svg>
  <div class="foot-link" style="left:968px;top:370px">support@lrr-law.com</div>

  <div class="abs" style="left:85px;top:500px;width:1030px;height:1px;background:#22395c"></div>
  <div class="abs" style="left:0;width:1200px;top:525px;text-align:center;font-size:13px;letter-spacing:2.5px;color:#4e6383">COPYRIGHT © 2023 LRR. ALL RIGHTS RESERVED.</div>
</footer>

</body>
</html>
```